International trading company needs banner designs for university careers fairs. Additional work to

Description
Our company, Meridale Capital, operates in the finance industry. We trade numerous financial instruments across the globe. We focus on futures, options, etfs and are currently expanding into the exciting area of cryptocurrencies. A main focus of ours is to use a systematic and quantitative approach to trading to develop and refine trading strategies that are relatively low risk in nature, but are scalable and provide positive returns. We work hard, we push each other to achieve great results. But at the same time we really enjoy each other’s company and share a relaxed atmosphere at work. Our website is http://www.meridalecapital.com.au/. Meridale will be attending university careers fairs and expos in coming months to attract the very best talent there is for graduate trading roles as well as graduate developer roles. As such, we require our booth to look professional. We want to convey our message that a career with us is exciting, rewarding, but also challenging. We aim to nurture talent and hope to provide the tools necessary to strive in a career in trading.

We have 3 aspects to our booth concept. But for this designer contest, we will focus on 1 of those projects. When we decide on one designer, we hope they will be willing to work one on one on the other 2 projects. On top of this contest, we are willing to pay $250 for the additional 2 projects, one of which is quite simple in design brief, the other will allow the designer the flare to be creative. It is important to note that all three concepts need to be cohesive. Each concept should complement the other in colour as well as message.

For the entire project to be finished, we are a little rushed on time and would require completion of all three concepts by February 2nd.

We will only require soft copy files so we can manage the print ourselves. We can accept a vector, eps or ai file.

For this contest project, the design concept is a pull-up banner. We will have 3 pull-up banners each with slightly different messages.

We have attached pictures to help inspire the designer. Also, we have attached company logo (a unicorn) and name, along with varying colour vectors.

Meridale Capital’s primary colours are black, green and white. We would like all 3 banners to be in the same scheme. But we are happy to see slightly different variations in design options on the colour scheme. We do feel that green writing on black background would look the sharpest and have the most impact. We could be wrong though and are fine to see different designs.

The banner dimensions will be 85cm wide x 210cm tall. So there is room on the banner to deliver an exciting, yet professional message.

Preliminary Pull-up Banner ideas
We are not designers, we are open to you, the designer, using your creative flare to design 3 sharp looking banners. We do have a rough idea of the direction of each banner though.

Banner 1 – A company inspired banner. We would like our company name, our logo (prominent!) and beneath it 3 to 4 words that describe what we’re about. For example, Challenging, Rewarding, Passionate, Entrepreneurial, Focused, Collaborative, Innovative, Systematic, Strategic. Happy for the designer to take control here.

For the rest of the banner we are open to design. Potentially a picture taken from our website that is reflective of our culture – which is relaxed, hard-working, collaborative, rewarding.

It doesn’t need to be too busy or cluttered, so no need to throw in designs that aren’t really consistent with us.

Banner 2 – A trader inspired banner. This is more designed to attract graduates interested in a career in trading. Include meridale name and logo. Maybe include a question for the students... Something like,
“Want to be challenged?
Want to strategise?
Want to be rewarded?
Become a trader!”
Doesn’t have to be straight angles, can be on an angle – designer free reign here. Also we can have different sentences, words. Up to the designer. We would like to include something that would attract a trader’s mind, something visual, like a trading chart. See attached pictures for trading chart examples.

Somewhere on the banner we can mention Graduate Trader Program, please contact us at careers@meridalecapital.com.au. Phone number below it (02) 7156 4830.

Banner 3 - A developer inspired banner. This is more designed to attract graduates interested in a career in developing. Include meridale name and logo

Put the following pitch on the banner and fill the rest of the space with designs and pictures. No fixed layout required here.

Good at problem solving? Obsessed with creating quality software? Love working with numbers? Do you speak programming language? Want to face fresh challenges each day?

On the banner we can mention Graduate Software Engineer Program, please contact us at careers@meridalecapital.com.au. Phone number below it (02) 7156 4830.

Additionally to the above 3 banners, we had an idea of including random words across the banners in random sizes and boldness. We’re not sure how this would appear so we would like to see a couple designs on this. We thought we could have a top tier of buzz words that should be more prominent with the second tier buzzwords in smaller size. Two design types - randomly displayed, secondly a bit more structured. Can decide what looks best when we receive design. Words below. We don’t have to include all of these words, whatever a good design lends itself to. Words should only be in green, black or white - consistent with our company scheme.

Top Tier Buzzwords
Trading
Cryptocurrency
Options
Market making
Trading
Bitcoin
Derivatives
ETF
Futures
Volatility
Arbitrage
Technology
HFT
Hedging

Second Tier Buzzwords
R&K 400
QMB 300
VLZ
DWT
QMB
FX
Bid
Offer
Margining
Long
Short
Spot
Position
Tolvar
Brimo
Wel Daro
WDI
GGI
Buy
Sell
Delta
Gamma
Vega
Theta
Skew
Straddle
Call

Once we have selected the designer, we are keen that they would complete another 2 projects for us. The other 2 projects are as follows:
• A double sided A5 flyer design – This should provide more information about what Meridale can offer the students as a career and a workplace. We will also give a small amount of detail about the graduate program.
• Table Cloth design – At each exhibition we receive a table at our booth. We would like to have a logo laden table cloth that will look professional

We would like the design scheme to flow neatly from the banners to the flyers to the table cloth. So the colours are consistent and our general tone/message is also consistent.

We have attached pictures that should help the designer. Included pictures of pull-up banners, pictures of student careers fairs, flyers, table cloth dimensions, Meridale’s logos and colour vectors.

Preliminary Double sided A5 Flyer ideas.

We would need two designs – a trader design and a developer design.

Art file to be supplied PDF file with trim marks & 3mm bleed

With the flyer we would like to add a little more information about Meridale on the front page (which should be the same for the trader flyer and the developer flyer). On the back page we would be a little more detailed in the graduate program. Give dates, the onboarding process, rough program details/info.

Front Page – Include Meridale name, logo. Explanation of who we are - proprietary trading firm, using our own capital to trade financial instruments around the world. We trade futures, options, etfs and cryptocurrencies (can make more elaborate).

To make it sound interesting we’d like to explain potential for growth in certain markets. So something along the lines, of “We are seeing rapid expansion in certain markets. At meridale we are always looking for new strategies and talent to expand our already growing presence. Working with Meridale, you’ll get exposure and experience on all of these exciting markets which will greatly benefit you in your career progression” (Doesn’t need to be word for word)

We’d also like to mention some of the perks of working with us:
daily lunch provided
cafe coffee
 breakfast/snacks
 casual attire
 cash bonus half yearly
 competitive rates
 team dinners
 gym membership
 company trips
We’d like to use consistent colour schemes with our company, Black and Green. Some white could work in there. But not a necessity.
The designer can feel free to add in some sharp looking images.

Back Page Trader Flyer - We would like to give some more info on the positives of the trader program. We’re mainly focusing on the strengths of the program here – listed below.
• 1 on 1 training
• In-depth theory classes with practical applications
• Experienced traders providing the training
• Live trading within 3 months
• Ongoing mentoring
• Exposure to different markets/strategies
• Placed onto products that best suit their strengths
• Simulated trader training based on actual events

We should also add contact details for students to apply to.
For more information on the Graduate Trader Program
contact us at careers@meridalecapital.com.au.
Phone number (02) 7156 4830.

OR

To apply please send through your CV and academic transcript to careers@meridalecapital.com.au

We would also want this to look quite sharp, so adding in a trading graph could make it look exciting and attractive.

Back Page Developer Flyer
• 1 on 1 mentoring by senior software engineers
• Full SDLC exposure
• Extremely agile environment
• Direct interaction with business and stakeholders
• Multiple career paths for future growth

For more information on the Graduate Software Engineer Program
Contact us at careers@meridalecapital.com.au.

OR

Preliminary table cloth ideas.
We would need two designs before choosing one.

First design is a very simple design that would look professional. A plain black design with MERIDALE on the front in Green.

The second design is plain black, MERIDALE on the front in Green, similar to above. But we’d also like to see the words mentioned above in the top tier and second tier randomly across the table cloth. In different sizes and weightings.
We’ll see which design looks the best and choose one.

References to see the products we’d be using:
https://brontelsigns.com.au/products/pull-up-banners
https://www.quorvelprint.com.au/lpt/flyers-sizes.aspx?mk=flyers+design&rd=1
https://www.tallowbanners.com.au/outdoor/custom-table-throws/loose-printed-table-throws.html

Target Market(s)

University Graduates in IT, Engineering, Maths, Sciences, Business that would be interested in a career of trading financial instruments including cryptocurrency, options, futures, ETFs. We are also targeting developers in the same space.

Industry/Entity Type

Finance

Font styles to use
Serif
Sans Serif

Colors
00a990
ffffff
000000
33b8a4
1b1b1b

Requirements
Must have
• Cohesion between banners and other project work.
• Clear message coming through
• Professional look
• Eye catching
• Attractive
• Colour schemes must work
Should not have
• Must not be boring. We are looking to project our company image. We are not boring so we want to see some creative flare. But we are also a professional firm so our designs must be sharp.

```html
<!DOCTYPE html>
<html lang="en">
<head>
<meta charset="utf-8">
<title>Meridale Capital – Graduate Trader Program Pull-up Banner</title>
<link href="https://fonts.googleapis.com/css2?family=Saira+Condensed:wght@300;600;700&family=Saira:wght@600&family=Orbitron:wght@500&display=swap" rel="stylesheet">
<style>
  :root {
    --green: #33b8a4;
    --green-deep: #00a990;
    --ink: #1b1b1b;
    --black: #000000;
    --white: #ffffff;
    --stage: #e4e5e7;
    --chart-dark: #061a5a;
    --chart-mid: #0b3fd0;
    --chart-light: #1f7cff;
  }
  * { margin: 0; padding: 0; box-sizing: border-box; }
  html, body { width: 1200px; height: 800px; overflow: hidden; }
  body {
    background: radial-gradient(ellipse at 50% 40%, #f1f2f3 0%, var(--stage) 70%);
    font-family: "Saira Condensed", "Arial Narrow", sans-serif;
    position: relative;
  }
  .banner {
    position: absolute;
    left: 410px;
    top: 32px;
    width: 380px;
    height: 736px;
    background: var(--ink);
    color: var(--white);
    text-align: center;
    overflow: hidden;
  }
  .banner__cap {
    position: absolute; left: 0; right: 0; height: 13px; background: var(--green);
  }
  .banner__cap--top { top: 0; }
  .banner__cap--bottom { bottom: 0; height: 16px; }
  .values {
    position: absolute; top: 50px; left: 0; right: 0;
    font-weight: 700; font-size: 21px; letter-spacing: 0.8px; line-height: 31px;
    text-transform: uppercase;
  }
  .values .divider {
    display: inline-block; width: 2px; height: 19px; background: var(--green);
    margin: 0 7px; vertical-align: -3px;
  }
  .brand {
    position: absolute; top: 140px; left: 0; right: 0;
    display: flex; flex-direction: column; align-items: center;
  }
  .brand__mark {
    width: 118px; height: 118px; border-radius: 50%; background: var(--green);
  }
  .brand__name {
    margin-top: 36px;
    font-weight: 300; font-size: 38px; letter-spacing: 4px; color: var(--white);
  }
  .program {
    position: absolute; top: 381px; left: 0; right: 0; height: 43px;
    background: var(--green);
    font-weight: 700; font-size: 25px; line-height: 43px; letter-spacing: 0.6px;
    color: #f4fbf9;
  }
  .contact {
    position: absolute; top: 444px; left: 0; right: 0;
  }
  .contact__lead { font-family: "Saira", sans-serif; font-weight: 600; font-size: 15px; line-height: 22px; }
  .contact__email { font-family: "Saira", sans-serif; font-weight: 600; font-size: 15.5px; line-height: 24px; }
  .contact__phone {
    font-family: "Orbitron", sans-serif; font-weight: 500; font-size: 25px;
    letter-spacing: 5px; color: var(--green); margin-top: 6px;
  }
  .market-wave {
    position: absolute; left: 0; bottom: 16px; width: 380px; height: 240px;
  }
</style>
</head>
<body>
  <main class="banner">
    <div class="banner__cap banner__cap--top"></div>

    <p class="values">
      Challenging<span class="divider"></span>Rewarding<br>
      Passionate<span class="divider"></span>Entrepreneurial
    </p>

    <div class="brand">
      <div class="brand__mark"></div>
      <div class="brand__name">MERIDALE</div>
    </div>

    <div class="program">Graduate Trader Program</div>

    <div class="contact">
      <p class="contact__lead">contact us at</p>
      <p class="contact__email">careers@meridalecapital.com.au</p>
      <p class="contact__phone">(02) 7156 4830</p>
    </div>

    <svg class="market-wave" viewBox="0 0 380 240" aria-hidden="false">
      <defs>
        <linearGradient id="chartFill" x1="0" y1="1" x2="1" y2="0">
          <stop offset="0" stop-color="var(--chart-dark)"/>
          <stop offset="0.55" stop-color="var(--chart-mid)"/>
          <stop offset="1" stop-color="var(--chart-light)"/>
        </linearGradient>
      </defs>
      <path role="img" aria-label="Blue digital trading chart with grid lines, binary figures and a rising arrow"
            d="M0 240 L0 205 C40 135 150 120 250 100 C330 85 365 45 380 0 L380 240 Z"
            fill="url(#chartFill)"/>
      <path d="M0 205 C40 135 150 120 250 100 C330 85 365 45 380 0"
            fill="none" stroke="var(--green-deep)" stroke-width="5"/>
    </svg>

    <div class="banner__cap banner__cap--bottom"></div>
  </main>
</body>
</html>
```